Tavenorix - world unique technology for better life - please let them know who am i at first sight

We need a new business card for company which is a provider of unique crystal based technology suitable for all living being. For more information and final design you can use our brochure (our colours are black and blue from brochure).
We use Verdana font

Industry/Entity Type

Business

Contact Information for Business Card

regular dimension

Font styles to use
Other font styles liked:
• Verdana

Requirements
Must have
• Logo
• name
• function/position
• phone
• mobile
• e-mail
• adress
Nice to have
• inovative design (technology directed)

```html
<!DOCTYPE html>
<html lang="en">
<head>
<meta charset="utf-8">
<title>Tavenorix Technologies – Business Card</title>
<link rel="stylesheet" href="https://fonts.googleapis.com/css2?family=Open+Sans:wght@300;400;600&display=swap">
<style>
  :root {
    --bg: #e8eaeb;
    --card: #ffffff;
    --blue: #27bfe3;
    --blue-deep: #1aa6d4;
    --grey: #8a9399;
    --white: #ffffff;
  }
  * { box-sizing: border-box; margin: 0; padding: 0; }
  html, body { width: 1200px; height: 858px; overflow: hidden; }
  body {
    background: var(--bg);
    font-family: "Open Sans", Verdana, sans-serif;
    display: flex;
    align-items: center;
    justify-content: center;
    gap: 44px;
  }
  .card {
    position: relative;
    width: 530px;
    height: 320px;
    background: linear-gradient(160deg, #ffffff 0%, #f3f4f5 100%);
    box-shadow: 0 6px 18px rgba(0,0,0,.14);
    overflow: hidden;
  }
  .band {
    position: absolute;
    left: 0; right: 0;
    background: linear-gradient(90deg, var(--blue-deep) 0%, var(--blue) 50%, var(--blue-deep) 100%);
  }
  .band::before, .band::after {
    content: "";
    position: absolute;
    left: 0; right: 0;
    height: 2px;
    background: var(--white);
  }
  .band::before { top: 5px; }
  .band::after { bottom: 5px; }
  .rule {
    position: absolute;
    left: 0; right: 0;
    height: 2px;
    background: var(--blue);
  }

  /* front */
  .front .band { top: 150px; height: 136px; }
  .front .rule { top: 296px; }
  .brand {
    position: absolute;
    left: 28px; top: 42px;
    display: flex;
    align-items: center;
    gap: 14px;
  }
  .brand-dot {
    width: 48px; height: 48px;
    border-radius: 50%;
    background: var(--blue);
  }
  .brand-name {
    font-weight: 300;
    font-size: 34px;
    letter-spacing: 1px;
    color: var(--blue);
    line-height: 1;
  }
  .brand-tag {
    margin-top: 6px;
    font-size: 10px;
    letter-spacing: 8px;
    color: var(--grey);
  }
  .person {
    position: absolute;
    right: 30px; top: 44px;
    text-align: left;
  }
  .person-name { font-size: 20px; font-weight: 600; color: var(--blue); }
  .person-role { font-size: 12px; color: var(--grey); margin-left: 46px; }
  .address {
    position: absolute;
    left: 28px; bottom: 20px;
    color: var(--white);
    font-size: 13px;
    line-height: 1.45;
  }
  .contacts {
    position: absolute;
    right: 30px; top: 20px;
    list-style: none;
    color: var(--white);
    font-size: 13px;
    line-height: 1.65;
  }
  .contacts li { display: flex; align-items: center; justify-content: flex-end; gap: 10px; }
  .contacts svg { width: 14px; height: 14px; flex: none; }

  /* back */
  .back .band { top: 82px; height: 156px; }
  .back .rule.top { top: 72px; }
  .back .rule.bottom { top: 246px; }
  .back-brand {
    position: absolute;
    inset: 0;
    display: flex;
    align-items: center;
    justify-content: center;
    gap: 16px;
  }
  .back-brand .brand-dot { width: 56px; height: 56px; background: var(--white); }
  .back-brand .brand-name { color: var(--white); font-size: 38px; }
  .back-brand .brand-tag { color: var(--white); }
</style>
</head>
<body>
  <section class="card front">
    <div class="brand">
      <span class="brand-dot"></span>
      <div>
        <div class="brand-name">TAVENORIX</div>
        <div class="brand-tag">TECHNOLOGIES</div>
      </div>
    </div>
    <div class="person">
      <div class="person-name">Employee Name</div>
      <div class="person-role">Managing Director</div>
    </div>
    <div class="band">
      <ul class="contacts">
        <li>+ xxx(x) xx xxx xxx
          <svg viewBox="0 0 14 14"><rect x="3.5" y="1" width="7" height="12" rx="1.2" fill="none" stroke="#fff" stroke-width="1.4"/><circle cx="7" cy="11" r=".8" fill="#fff"/></svg>
        </li>
        <li>+44(0) 20 7946 031
          <svg viewBox="0 0 14 14"><path d="M3 1.5l2.2 2.6-1.3 1.5a8 8 0 0 0 4.5 4.5l1.5-1.3 2.6 2.2-1.4 1.5C6 12.5 1.5 8 1.5 2.9z" fill="#fff"/></svg>
        </li>
        <li>info@tavenorix.eu
          <svg viewBox="0 0 14 14"><rect x="1" y="3" width="12" height="8.5" fill="none" stroke="#fff" stroke-width="1.4"/><path d="M1 3l6 5 6-5" fill="none" stroke="#fff" stroke-width="1.4"/></svg>
        </li>
      </ul>
      <address class="address" style="font-style:normal">
        28 Marlow Yard<br>
        London EC2A 7QT, United Kingdom
      </address>
    </div>
    <div class="rule"></div>
  </section>

  <section class="card back">
    <div class="rule top"></div>
    <div class="band"></div>
    <div class="rule bottom"></div>
    <div class="back-brand">
      <span class="brand-dot"></span>
      <div>
        <div class="brand-name">TAVENORIX</div>
        <div class="brand-tag">TECHNOLOGIES</div>
      </div>
    </div>
  </section>
</body>
</html>
```